lab equipment website

We need a fresh new look for a company website called quorvin. We will be using the current logo and brand colors on their current website quorvin.com. They want to keep their text and on-page SEO, but would like to reformat it to look more modern and fresh. They want to have everything be high performance with a great user experience. Their main call to action is for people to fill in a contact form so they can call them. There is some information that is purposely above the fold on the instrument pages. I will need the home page, about page and a leasing page.

```html
<!DOCTYPE html>
<html lang="en">
<head>
<meta charset="utf-8">
<title>quorvin — Lab Equipment Service & Leasing</title>
<link href="https://fonts.googleapis.com/css2?family=Jost:ital,wght@0,400;0,500;0,600;1,400&display=swap" rel="stylesheet">
<style>
:root{
  --teal:#00b89c;
  --teal-dark:#2f5d66;
  --ink:#1f2a30;
  --text:#5b6670;
  --muted:#8a949c;
  --panel:#f1f3f4;
  --footer:#2b2f36;
  --field:#6f737a;
  --white:#ffffff;
}
*{box-sizing:border-box;margin:0;padding:0}
html,body{width:1200px;height:3371px;overflow:hidden}
body{font-family:"Jost",Arial,sans-serif;color:var(--ink);background:var(--white);position:relative}
.abs{position:absolute}
a{color:inherit;text-decoration:none}

/* header */
.site-header{position:absolute;left:0;top:0;width:1200px;height:112px;background:var(--white)}
.brand{position:absolute;left:88px;top:26px;display:flex;align-items:center;gap:12px}
.brand-mark{width:28px;height:28px;border-radius:50%;background:var(--teal)}
.brand-name{font-size:36px;font-weight:600;color:var(--ink);line-height:1}
.brand-tag{position:absolute;left:128px;top:64px;font-size:12px;line-height:13px;color:var(--teal)}
.topbar{position:absolute;right:88px;top:20px;display:flex;align-items:center;gap:24px;font-size:14px;color:var(--text)}
.topbar b{color:var(--teal);font-weight:500}
.social-dots{display:flex;gap:9px}
.social-dots span{width:12px;height:12px;border-radius:50%;border:1.5px solid var(--teal)}
.main-nav{position:absolute;left:440px;top:64px;display:flex;gap:0;font-size:14px;color:var(--text)}
.main-nav a{width:102px;text-align:center}
.main-nav a.is-active{color:var(--teal)}
.btn-outline{position:absolute;left:950px;top:58px;width:162px;height:34px;border:1.5px solid var(--teal);color:var(--teal);font-size:14px;font-weight:500;display:flex;align-items:center;justify-content:center}

/* hero */
.hero{position:absolute;left:0;top:112px;width:1200px;height:488px;background:linear-gradient(90deg,#dfe9ef 0%,#cfdfe8 45%,#b7c7cf 75%,#8e9ca3 100%)}
.hero-title{position:absolute;left:88px;top:146px;font-size:35px;line-height:40px;font-weight:400;color:var(--ink)}
.hero-title strong{font-weight:600}
.btn-solid{background:var(--teal);color:var(--white);font-size:14px;font-weight:500;display:flex;align-items:center;justify-content:center}
.hero .btn-solid{position:absolute;left:88px;top:300px;width:192px;height:31px}
.dots{display:flex;gap:8px}
.dots span{width:11px;height:11px;border-radius:50%;border:1.5px solid var(--white)}
.hero .dots{position:absolute;left:562px;top:412px}
.dots.dark span{border-color:var(--teal)}

/* needs */
.needs{position:absolute;left:0;top:600px;width:1200px;height:592px}
.needs-copy{position:absolute;left:88px;top:72px;width:620px}
.needs-copy h2{font-size:31px;line-height:40px;font-weight:400;color:var(--ink);margin-bottom:22px}
.needs-copy p{font-size:12px;line-height:17px;color:var(--text)}
.checklist{list-style:none;margin:26px 0 26px 44px;border-left:1px solid #dfe3e6;padding-left:16px}
.checklist li{font-size:12.5px;line-height:17px;color:var(--text);padding-left:22px;position:relative;margin-bottom:12px}
.checklist li svg{position:absolute;left:0;top:2px}
.needs-copy .link{color:var(--teal);text-decoration:underline}
.goal-panel{position:absolute;left:800px;top:0;width:400px;height:592px;background:linear-gradient(180deg,#ffffff 0%,var(--panel) 40%,#e4e8ea 100%)}
.goal-icon{position:absolute;left:80px;top:75px;width:34px;height:34px;border-radius:50%;background:var(--teal)}
.goal-panel h3{position:absolute;left:80px;top:134px;width:260px;font-size:25px;line-height:30px;font-weight:600}
.goal-rule{position:absolute;left:80px;top:245px;width:80px;height:2px;background:var(--teal)}
.goal-panel p{position:absolute;left:80px;top:278px;width:220px;font-size:12.5px;line-height:19px;color:var(--text)}
.goal-link{position:absolute;left:80px;top:466px;font-size:13px;font-weight:500;display:flex;align-items:center;gap:14px}
.goal-link i{display:block;width:48px;height:1.5px;background:var(--ink)}

/* instruments */
.instruments{position:absolute;left:0;top:1192px;width:1200px;height:440px;background:linear-gradient(135deg,#3f6d75 0%,var(--teal-dark) 45%,#26484f 100%)}
.instruments h2{position:absolute;left:0;top:72px;width:1200px;text-align:center;font-size:32px;font-weight:400;color:var(--teal)}
.card{position:absolute;width:242px;height:63px;background:var(--white);display:flex;align-items:center;justify-content:space-between;padding:0 16px;font-size:15px;font-weight:500;color:var(--ink)}
.card span.arrow{width:12px;height:12px;border-radius:50%;border:1.2px solid var(--teal);position:relative}
.card span.arrow::after{content:"";position:absolute;left:3px;top:3.5px;width:3px;height:3px;border-right:1.2px solid var(--teal);border-top:1.2px solid var(--teal);transform:rotate(45deg)}
.card.is-active{background:var(--teal);color:var(--white)}
.card.is-active span.arrow{border-color:var(--white)}
.card.is-active span.arrow::after{border-color:var(--white)}
.slider-arrow{position:absolute;top:210px}
.btn-ghost{position:absolute;left:528px;top:329px;width:144px;height:32px;border:1.5px solid var(--white);color:var(--white);font-size:12.5px;font-weight:500;display:flex;align-items:center;justify-content:center}

/* testimonial */
.testimonial{position:absolute;left:0;top:1632px;width:1200px;height:475px;text-align:center}
.avatar{position:absolute;left:560px;top:82px;width:80px;height:80px;border-radius:50%;background:linear-gradient(160deg,#c9d3d8,#8b979d);border:3px solid var(--white);box-shadow:0 0 0 2px var(--teal)}
.quote-mark{position:absolute;top:80px;font-size:48px;font-weight:600;color:var(--teal);line-height:1}
.testimonial blockquote{position:absolute;left:250px;top:200px;width:700px;font-size:14px;line-height:24px;font-style:italic;color:var(--text)}
.testimonial .name{position:absolute;left:0;top:318px;width:1200px;font-size:15px;font-weight:600;color:var(--teal)}
.testimonial .role{position:absolute;left:0;top:340px;width:1200px;font-size:13px;color:var(--ink)}
.testimonial .dots{position:absolute;left:575px;top:378px}

/* features */
.features{position:absolute;left:0;top:2107px;width:1200px;height:479px}
.features-photo{position:absolute;left:0;top:0;width:600px;height:479px;background:linear-gradient(120deg,#d9e0e4 0%,#aab5bb 50%,#e9edef 100%)}
.features-panel{position:absolute;left:600px;top:0;width:600px;height:479px;background:var(--teal)}
.feature{position:absolute;left:600px;width:600px;height:80px}
.feature svg{position:absolute;left:-40px;top:0}
.feature p{position:absolute;left:72px;top:18px;width:420px;font-size:19px;line-height:24px;color:var(--white)}

/* contact cta */
.cta{position:absolute;left:0;top:2586px;width:1200px;height:332px;text-align:center}
.cta h2{position:absolute;left:0;top:72px;width:1200px;font-size:31px;font-weight:400}
.cta h2 strong{font-weight:600}
.cta p{position:absolute;left:260px;top:136px;width:680px;font-size:15px;line-height:22px;color:var(--text)}
.cta .btn-solid{position:absolute;left:521px;top:217px;width:144px;height:31px;font-size:12.5px}

/* footer */
.site-footer{position:absolute;left:0;top:2918px;width:1200px;height:453px;background:var(--footer);color:var(--white)}
.site-footer h4{position:absolute;top:77px;font-size:14px;font-weight:600}
.footer-phone{position:absolute;left:88px;top:128px;font-size:22px}
.footer-mail{position:absolute;left:88px;top:160px;font-size:12.5px}
.footer-addr{position:absolute;left:88px;top:198px;width:240px;font-size:12.5px;line-height:20px}
.footer-social{position:absolute;left:88px;top:266px;display:flex;gap:14px}
.footer-social span{width:28px;height:28px;border-radius:50%;border:1.5px solid var(--teal)}
.footer-social span.filled{background:var(--teal)}
.quick-links{position:absolute;left:420px;top:130px;list-style:none;font-size:12.5px;line-height:29px}
.quick-links .is-active{color:var(--teal)}
.field{position:absolute;top:133px;height:33px;background:var(--field);font-size:11.5px;padding:9px 10px;color:var(--white)}
.field.message{left:591px;top:181px;width:519px;height:103px}
.send{position:absolute;left:1055px;top:268px;width:32px;height:32px;border-radius:50%;background:var(--teal)}
.copyright{position:absolute;left:88px;top:363px;font-size:12px}
.copyright b{color:var(--teal);font-weight:400}
</style>
</head>
<body>

<header class="site-header">
  <a class="brand" href="#"><span class="brand-mark"></span><span class="brand-name">quorvin</span></a>
  <div class="brand-tag">your success,<br>our support.</div>
  <div class="topbar">
    <span><b>Call Us:</b> (555) 014-2297</span>
    <span><b>Email:</b> info@quorvin.com</span>
    <span class="social-dots"><span></span><span></span><span></span><span></span></span>
  </div>
  <nav class="main-nav">
    <a class="is-active" href="#">— Home —</a><a href="#">About Us</a><a href="#">Leasing</a><a href="#">FAQ</a><a href="#">Contact Us</a>
  </nav>
  <a class="btn-outline" href="#">Get A Free Quote</a>
</header>

<section class="hero" role="img" aria-label="Photo of a laboratory microscope in a bright lab">
  <h1 class="hero-title">Trusted Company <strong>Offering<br>Scientific Equipment Service</strong><br>Plans and <strong>Flexible Leases</strong></h1>
  <a class="btn-solid" href="#">Instruments &amp; Service</a>
  <div class="dots"><span style="background:#fff"></span><span></span><span></span><span></span></div>
</section>

<section class="needs">
  <div class="needs-copy">
    <h2>We Understand Your Needs Because We<br>are Scientists First</h2>
    <p>When it comes to creating innovative solutions that cater to your lab, quorvin's dedicated team of problem-solvers has got you covered. Here's how we save you time and money:</p>
    <ul class="checklist">
      <li><svg width="13" height="13" viewBox="0 0 13 13"><circle cx="6.5" cy="6.5" r="5.8" fill="none" stroke="#00b89c" stroke-width="1.2"/><path d="M3.8 6.6l1.8 1.8 3.6-3.6" fill="none" stroke="#00b89c" stroke-width="1.2"/></svg>We collaborate with you directly- no middlemen</li>
      <li><svg width="13" height="13" viewBox="0 0 13 13"><circle cx="6.5" cy="6.5" r="5.8" fill="none" stroke="#00b89c" stroke-width="1.2"/><path d="M3.8 6.6l1.8 1.8 3.6-3.6" fill="none" stroke="#00b89c" stroke-width="1.2"/></svg>We handle scientific equipment service, repairs, and maintenance</li>
      <li><svg width="13" height="13" viewBox="0 0 13 13"><circle cx="6.5" cy="6.5" r="5.8" fill="none" stroke="#00b89c" stroke-width="1.2"/><path d="M3.8 6.6l1.8 1.8 3.6-3.6" fill="none" stroke="#00b89c" stroke-width="1.2"/></svg>We consolidate and streamline the ancillary work associated with lab equipment procurement and service</li>
      <li><svg width="13" height="13" viewBox="0 0 13 13"><circle cx="6.5" cy="6.5" r="5.8" fill="none" stroke="#00b89c" stroke-width="1.2"/><path d="M3.8 6.6l1.8 1.8 3.6-3.6" fill="none" stroke="#00b89c" stroke-width="1.2"/></svg>We utilize our networks to bring you the most cost-savings possible</li>
      <li><svg width="13" height="13" viewBox="0 0 13 13"><circle cx="6.5" cy="6.5" r="5.8" fill="none" stroke="#00b89c" stroke-width="1.2"/><path d="M3.8 6.6l1.8 1.8 3.6-3.6" fill="none" stroke="#00b89c" stroke-width="1.2"/></svg>We improve cash flow by removing the upfront cost of purchasing, freeing up capital in your everyday budget</li>
      <li><svg width="13" height="13" viewBox="0 0 13 13"><circle cx="6.5" cy="6.5" r="5.8" fill="none" stroke="#00b89c" stroke-width="1.2"/><path d="M3.8 6.6l1.8 1.8 3.6-3.6" fill="none" stroke="#00b89c" stroke-width="1.2"/></svg>We may provide tax advantages with our lease structures</li>
    </ul>
    <p>We regularly provide businesses with what they need to improve their budget and efficiency. We offer <a class="link" href="#">laboratory equipment leasing</a> for a wide range of needs. If you want to discuss your needs more in-depth, don't hesitate to call us at (555) 014-2297 or fill out our <a class="link" href="#">contact form</a>.</p>
  </div>
  <aside class="goal-panel">
    <span class="goal-icon"></span>
    <h3>Our goal is a save labs time and money</h3>
    <span class="goal-rule"></span>
    <p>quorvin is a lab support program that provides scientists with comprehensive maintenance/repair coverage and operating lease solutions at an affordable price.</p>
    <a class="goal-link" href="#">Discover About Us <i></i></a>
  </aside>
</section>

<section class="instruments">
  <h2>Instruments &amp; Service</h2>
  <svg class="slider-arrow" style="left:34px" width="16" height="20" viewBox="0 0 16 20"><path d="M12 2L4 10l8 8" fill="none" stroke="#00b89c" stroke-width="2"/></svg>
  <svg class="slider-arrow" style="left:1150px" width="16" height="20" viewBox="0 0 16 20"><path d="M4 2l8 8-8 8" fill="none" stroke="#00b89c" stroke-width="2"/></svg>
  <a class="card" style="left:88px;top:148px" href="#">Autoclave<span class="arrow"></span></a>
  <a class="card" style="left:348px;top:148px" href="#">Lab Balance<span class="arrow"></span></a>
  <a class="card" style="left:608px;top:148px" href="#">Centrifuge<span class="arrow"></span></a>
  <a class="card" style="left:868px;top:148px" href="#">Microscope<span class="arrow"></span></a>
  <a class="card" style="left:88px;top:226px" href="#">Cryostat<span class="arrow"></span></a>
  <a class="card is-active" style="left:348px;top:226px" href="#">Flow Cytometer<span class="arrow"></span></a>
  <a class="card" style="left:608px;top:226px" href="#">Pcr Systems<span class="arrow"></span></a>
  <a class="card" style="left:868px;top:226px" href="#">Liquid Handler<span class="arrow"></span></a>
  <a class="btn-ghost" href="#">View All Leasing</a>
</section>

<section class="testimonial">
  <span class="quote-mark" style="left:540px">“</span>
  <div class="avatar" role="img" aria-label="Portrait of the quoted team member"></div>
  <span class="quote-mark" style="left:632px;top:130px">”</span>
  <blockquote>My time spent in the lab opened my eyes to the passion and dedication that drives scientists, as well as the frustration of a tight budget and equipment upkeep. quorvin was created in order to help overcome those obstacles and enable scientists to focus on what they're truly passionate about: research.</blockquote>
  <div class="name">Dana Morlet</div>
  <div class="role">Lab Relations</div>
  <div class="dots dark"><span style="background:#00b89c"></span><span></span><span></span></div>
</section>

<section class="features">
  <div class="features-photo" role="img" aria-label="Photo of a gloved hand loading a tray into an open autoclave"></div>
  <div class="features-panel"></div>
  <div class="feature" style="top:90px">
    <svg width="80" height="80" viewBox="0 0 80 80"><path d="M40 4l31 18v36L40 76 9 58V22z" fill="#00b89c" stroke="#fff" stroke-width="3"/><rect x="28" y="32" width="24" height="18" rx="2" fill="none" stroke="#fff" stroke-width="2"/><path d="M40 36v10M35 41h10" stroke="#fff" stroke-width="2"/></svg>
    <p>Worry free lab equipment PM/repair coverage.</p>
  </div>
  <div class="feature" style="top:194px">
    <svg width="80" height="80" viewBox="0 0 80 80"><path d="M40 4l31 18v36L40 76 9 58V22z" fill="#00b89c" stroke="#fff" stroke-width="3"/><path d="M32 28v10a7 7 0 0014 0V28M39 45v4a7 7 0 0014 0v-5" fill="none" stroke="#fff" stroke-width="2"/><circle cx="53" cy="42" r="3" fill="none" stroke="#fff" stroke-width="2"/></svg>
    <p>Cost-effective lease structures and payment plans.</p>
  </div>
  <div class="feature" style="top:312px">
    <svg width="80" height="80" viewBox="0 0 80 80"><path d="M40 4l31 18v36L40 76 9 58V22z" fill="#00b89c" stroke="#fff" stroke-width="3"/><path d="M35 26h10M37 26v12l-9 14h24l-9-14V26" fill="none" stroke="#fff" stroke-width="2"/></svg>
    <p>Knowledge of the laboratory.</p>
  </div>
</section>

<section class="cta">
  <h2>Further <strong>Questions?</strong></h2>
  <p>Feel free to contact us if you have any questions or comments. We promise to get back to you within 24 hours.</p>
  <a class="btn-solid" href="#">Contact Us</a>
</section>

<footer class="site-footer">
  <h4 style="left:88px">Contact Us</h4>
  <div class="footer-phone">Call: (555) 014-2297</div>
  <div class="footer-mail">info@quorvin.com</div>
  <div class="footer-addr">48 Harbor Lane, Suite 310, Eastfield, CA 94000</div>
  <div class="footer-social"><span></span><span class="filled"></span><span></span><span></span></div>
  <h4 style="left:420px">Quick Links</h4>
  <ul class="quick-links">
    <li>Home</li><li class="is-active">About Us</li><li>Leasing</li><li>FAQs</li><li>Contact Us</li>
  </ul>
  <h4 style="left:591px">Get A Free Quote</h4>
  <div class="field" style="left:591px;width:169px">Name</div>
  <div class="field" style="left:771px;width:162px">Phone</div>
  <div class="field" style="left:946px;width:164px">Email</div>
  <div class="field message">Message ...</div>
  <span class="send"><svg width="32" height="32" viewBox="0 0 32 32"><path d="M11 10l12 6-12 6 2-6z" fill="#fff"/></svg></span>
  <div class="copyright">©2019 <b>quorvin.com</b> All Rights Reseved</div>
</footer>

</body>
</html>
```